Wohnhof am Weiher - Zeitungsinserat für den Verkauf von Eigentumswohnungen

Wir brauchen ein Zeitungsinserat in zwei Formaten. Einmal 296 Breite x 440 Höhe mm und einmal 296 Breite x 220 mm Höhe.
Als Basis dient der sehr grobe Entwurf im Powerpoint (Entwurf.pptx).
Auf dem Entwurf fehlen noch die Kontaktangeben:
Brunnhofer Liegenschaften AG
Seematteweg 14
4387 Tannried
079 462 37 58
rbrunnhofer@tessin-ostwald.ch

Zudem muss noch der Link auf die Webseite aufgeführt werden.
www.wohnhof-am-weiher.ch

Zudem fehlt noch der Text:
Fordern Sie noch heute die Verkaufsunterlagen gedruckt oder per Email an. Schreiben Sie uns einfach eine Chatpost mit Ihrer Adresse.

Ich habe noch Files von den Innenvisualisierungen, den Aussenvisualisierungen sowie unser Logo hinzugefügt. Zudem habe ich Ihnen die Verkaufsbrochure angefügt. Sie können die Daten vom Entwurf gerne ergänzen wenn Ihnen etwas gefällt. Schön wäre es, wenn Sie den Stil ähnlich machen würden wie die Brochure.

Target Market(s)

Famillien, Paare und Rentner

Font styles to use
Serif

Colors

Designer to choose colors to be used in the design.

Requirements
Must have
• Tolles Design das sofort anspricht!

```html
<!DOCTYPE html>
<html lang="de">
<head>
<meta charset="utf-8">
<title>Wohnhof am Weiher – Inserat</title>
<link rel="stylesheet" href="https://fonts.googleapis.com/css2?family=Montserrat:wght@300;400;500;700;900&display=swap">
<style>
  :root {
    --backdrop: #e6dacd;
    --paper: #ffffff;
    --slate: #36434b;
    --red: #e3202a;
    --blue: #3d86ad;
    --navy: #2f4556;
    --table-bg: #d9d4cf;
    --table-line: #ffffff;
    --ink: #3a3a3a;
    --tick: #9acd32;
  }
  * { box-sizing: border-box; margin: 0; padding: 0; }
  html, body { width: 1200px; height: 800px; overflow: hidden; }
  body {
    background: var(--backdrop);
    font-family: "Montserrat", sans-serif;
    display: flex; align-items: center; justify-content: center;
  }
  .ad {
    position: relative; width: 525px; height: 780px;
    background: var(--paper); overflow: hidden;
    box-shadow: 0 6px 24px rgba(0,0,0,.18);
  }
  /* header */
  .ad-header { position: absolute; inset: 0 0 auto 0; height: 96px; }
  .corner-texture {
    position: absolute; width: 120px; height: 80px;
    background: radial-gradient(circle at 0 0, rgba(120,120,120,.28), rgba(255,255,255,0) 70%);
  }
  .corner-texture.left { left: 0; top: 10px; }
  .corner-texture.right { right: 0; top: 0; transform: scaleX(-1); }
  .brand {
    position: absolute; top: 36px; left: 0; right: 0; text-align: center;
    color: var(--blue); font-weight: 700; font-size: 17px; letter-spacing: 1.5px;
  }
  .red-rule { position: absolute; top: 86px; left: 120px; right: 0; height: 8px; background: var(--red); }

  /* hero */
  .hero { position: absolute; top: 94px; left: 0; right: 0; height: 250px; background: var(--slate); }
  .hero-photo {
    position: absolute; top: 0; right: 0; width: 300px; height: 100%;
    background: linear-gradient(180deg, #8a9aa4 0%, #a7b0aa 45%, #4f7a3a 70%, #35592a 100%);
    clip-path: polygon(30% 0, 100% 0, 100% 100%, 0 100%);
  }
  .hero-text { position: absolute; left: 30px; top: 48px; color: #fff; }
  .title-strong { font-weight: 900; font-size: 38px; line-height: 1; letter-spacing: 1px; }
  .title-light { font-weight: 300; font-size: 36px; line-height: 1.05; letter-spacing: 1px; }
  .subtitle { margin-top: 8px; font-size: 11.5px; font-weight: 400; letter-spacing: 1.2px; line-height: 1.3; }
  .features { display: flex; gap: 22px; margin-top: 14px; font-size: 10px; font-weight: 300; letter-spacing: .6px; }
  .features ul { list-style: none; }
  .features li { display: flex; align-items: center; gap: 6px; line-height: 1.6; }
  .features svg { width: 11px; height: 11px; flex: none; }
  .red-diagonal {
    position: absolute; left: 0; right: 0; top: 322px; height: 30px; background: var(--red);
    clip-path: polygon(0 78%, 100% 0, 100% 22%, 0 100%);
  }

  /* interiors */
  .interiors {
    position: absolute; top: 340px; left: 0; right: 0; height: 150px;
    background: linear-gradient(100deg, #6f665d 0%, #c9c2b8 35%, #e9e6e1 60%, #b7b1aa 100%);
    clip-path: polygon(0 8%, 100% 0, 100% 100%, 0 100%);
  }

  /* call to action */
  .cta {
    position: absolute; top: 478px; left: 0; right: 0; height: 44px; background: var(--blue);
    color: #fff; text-align: center; font-size: 9.5px; font-weight: 400; letter-spacing: .5px;
    line-height: 1.4; padding-top: 9px;
  }

  /* tables */
  .units {
    position: absolute; top: 530px; left: 12px; right: 12px;
    display: grid; grid-template-columns: repeat(3, minmax(0, 1fr)); gap: 8px;
  }
  .house { min-width: 0; background: var(--table-bg); }
  .house h2 {
    background: var(--navy); color: #fff; font-weight: 900; font-size: 12px;
    text-align: center; padding: 3px 0; letter-spacing: 1px;
  }
  .house table {
    width: 100%; table-layout: fixed; border-collapse: collapse;
    font-size: 5.2px; color: var(--ink); line-height: 1.25;
  }
  .house col.floor { width: 18%; }
  .house col.rooms { width: 14%; }
  .house col.area { width: 13%; }
  .house col.outdoor { width: 28%; }
  .house col.price { width: 27%; }
  .house td { padding: 4px 2px; vertical-align: top; border-bottom: 1px solid var(--table-line); overflow-wrap: break-word; }
  .house td:first-child { padding-left: 3px; }
  .house tr:last-child td { border-bottom: 0; }
  .house td.price { text-align: right; white-space: nowrap; padding-right: 3px; }

  /* footer */
  .contact {
    position: absolute; left: 0; right: 0; bottom: 0; height: 78px; background: var(--blue); color: #fff;
    display: grid; grid-template-columns: 1fr 1fr; align-content: center; gap: 8px 10px;
    padding: 0 22px; font-size: 11px; font-weight: 400; letter-spacing: .4px;
  }
  .contact div { display: flex; align-items: center; gap: 7px; }
  .contact svg { width: 14px; height: 14px; flex: none; }
</style>
</head>
<body>
<article class="ad">
  <header class="ad-header">
    <div class="corner-texture left" role="img" aria-label="Dekoratives Punktraster"></div>
    <div class="corner-texture right" role="img" aria-label="Dekoratives Punktraster"></div>
    <div class="brand">BRUNNHOFER LIEGENSCHAFTEN AG</div>
    <div class="red-rule"></div>
  </header>

  <section class="hero">
    <div class="hero-photo" role="img" aria-label="Aussenvisualisierung der Wohnanlage mit Rasen und Bäumen"></div>
    <div class="hero-text">
      <div class="title-strong">WOHNHOF</div>
      <div class="title-light">AM WEIHER</div>
      <p class="subtitle">HOCHWERTIGE UND MODERNE<br>EIGENTUMSWOHNUNGEN</p>
      <div class="features">
        <ul>
          <li><svg viewBox="0 0 12 12"><path d="M1 6.5 4.5 10 11 2" fill="none" stroke="var(--tick)" stroke-width="2"/></svg>Bus und Bahn</li>
          <li><svg viewBox="0 0 12 12"><path d="M1 6.5 4.5 10 11 2" fill="none" stroke="var(--tick)" stroke-width="2"/></svg>Basel - Stadt</li>
          <li><svg viewBox="0 0 12 12"><path d="M1 6.5 4.5 10 11 2" fill="none" stroke="var(--tick)" stroke-width="2"/></svg>Autobahn</li>
        </ul>
        <ul>
          <li><svg viewBox="0 0 12 12"><path d="M1 6.5 4.5 10 11 2" fill="none" stroke="var(--tick)" stroke-width="2"/></svg>Einkaufen und weitere<br>Dienstleistungen</li>
          <li><svg viewBox="0 0 12 12"><path d="M1 6.5 4.5 10 11 2" fill="none" stroke="var(--tick)" stroke-width="2"/></svg>Erholung im Grünen</li>
        </ul>
      </div>
    </div>
  </section>
  <div class="interiors" role="img" aria-label="Innenvisualisierungen: Wohnzimmer, Essbereich und Küche"></div>
  <div class="red-diagonal"></div>

  <p class="cta">Fordern Sie noch heute die Verkaufsunterlagen gedruckt oder per Email an.<br>Schreiben Sie uns einfach eine Chatpost mit Ihrer Adresse.</p>

  <section class="units">
    <div class="house">
      <h2>HAUS A</h2>
      <table>
        <colgroup><col class="floor"><col class="rooms"><col class="area"><col class="outdoor"><col class="price"></colgroup>
        <tr><td>Attika</td><td>4.5 Zimmer</td><td>108m²</td><td>105m² Sonnenterrasse</td><td class="price">945'000 CHF</td></tr>
        <tr><td>Ober­geschoss</td><td>3.5 Zimmer</td><td>81m²</td><td>16m² Balkon</td><td class="price">754'800 CHF</td></tr>
        <tr><td>Ober­geschoss</td><td>4.5 Zimmer</td><td>102m²</td><td>33m² Balkon</td><td class="price">640'000 CHF</td></tr>
        <tr><td>Erd­geschoss</td><td>3.5 Zimmer</td><td>81m²</td><td>16m² gedeckter Sitzplatz &amp; eigener Garten</td><td class="price">657'000 CHF</td></tr>
        <tr><td>Erd­geschoss</td><td>4.5 Zimmer</td><td>102m²</td><td>33m² gedeckter Sitzplatz &amp; eigener Garten</td><td class="price">765'000 CHF</td></tr>
      </table>
    </div>
    <div class="house">
      <h2>HAUS B</h2>
      <table>
        <colgroup><col class="floor"><col class="rooms"><col class="area"><col class="outdoor"><col class="price"></colgroup>
        <tr><td>Attika</td><td>4.5 Zimmer</td><td>109m²</td><td>107m² Sonnenterrasse</td><td class="price">965'000 CHF</td></tr>
        <tr><td>Ober­geschoss</td><td>2.5 Zimmer</td><td>69m²</td><td>14m² Balkon</td><td class="price">550'000 CHF</td></tr>
        <tr><td>Ober­geschoss</td><td>4.5 Zimmer</td><td>117m²</td><td>42m² Balkon</td><td class="price">877'500 CHF</td></tr>
        <tr><td>Erd­geschoss</td><td>2.5 Zimmer</td><td>69m²</td><td>14m² gedeckter Sitzplatz &amp; eigener Garten</td><td class="price">560'000 CHF</td></tr>
        <tr><td>Erd­geschoss</td><td>4.5 Zimmer</td><td>117m²</td><td>42m² gedeckter Sitzplatz &amp; eigener Garten</td><td class="price">889'000 CHF</td></tr>
      </table>
    </div>
    <div class="house">
      <h2>HAUS C</h2>
      <table>
        <colgroup><col class="floor"><col class="rooms"><col class="area"><col class="outdoor"><col class="price"></colgroup>
        <tr><td>Attika</td><td>4.5 Zimmer</td><td>129m²</td><td>132m² Sonnenterrasse</td><td class="price">1'125'000 CHF</td></tr>
        <tr><td>Ober­geschoss</td><td>5.5 Zimmer</td><td>143m²</td><td>43m² Balkon</td><td class="price">1'059'000 CHF</td></tr>
        <tr><td>Ober­geschoss</td><td>3.5 Zimmer</td><td>96m²</td><td>23m² Balkon</td><td class="price">730'000 CHF</td></tr>
        <tr><td>Erd­geschoss</td><td>5.5 Zimmer</td><td>143m²</td><td>43m² gedeckter Sitzplatz &amp; eigener Garten</td><td class="price">1'065'000 CHF</td></tr>
        <tr><td>Erd­geschoss</td><td>3.5 Zimmer</td><td>96m²</td><td>23m² gedeckter Sitzplatz &amp; eigener Garten</td><td class="price">740'000 CHF</td></tr>
      </table>
    </div>
  </section>

  <footer class="contact">
    <div><svg viewBox="0 0 14 14"><path d="M7 13s-4.5-4.6-4.5-7.8a4.5 4.5 0 0 1 9 0C11.5 8.4 7 13 7 13z" fill="none" stroke="#fff" stroke-width="1.2"/><circle cx="7" cy="5.3" r="1.6" fill="none" stroke="#fff" stroke-width="1.2"/></svg>Seematteweg 14, 4387 Tannried</div>
    <div><svg viewBox="0 0 14 14"><path d="M3 1.5h2.2l1 3-1.5 1a7 7 0 0 0 3.8 3.8l1-1.5 3 1v2.2A1.5 1.5 0 0 1 11 12.5 9.5 9.5 0 0 1 1.5 3 1.5 1.5 0 0 1 3 1.5z" fill="none" stroke="#fff" stroke-width="1.2"/></svg>079 462 37 58</div>
    <div><svg viewBox="0 0 14 14"><rect x="1" y="3" width="12" height="8.5" rx="1" fill="none" stroke="#fff" stroke-width="1.2"/><path d="M1.5 3.5 7 8l5.5-4.5" fill="none" stroke="#fff" stroke-width="1.2"/></svg>rbrunnhofer@tessin-ostwald.ch</div>
    <div><svg viewBox="0 0 14 14"><circle cx="7" cy="7" r="5.8" fill="none" stroke="#fff" stroke-width="1.2"/><path d="M1.2 7h11.6M7 1.2c-3 3.4-3 8.2 0 11.6M7 1.2c3 3.4 3 8.2 0 11.6" fill="none" stroke="#fff" stroke-width="1"/></svg>www.wohnhof-am-weiher.ch</div>
  </footer>
</article>
</body>
</html>
```